Mental Health care Company in Washington DC

We are a new mental health care services provider in Washington DC. Please look at these sites.
https://marlowbrookpartners.com
https://www.quillstoneinc.com
https://velmarsh-kt.org/
https://www.trivanqx.com
https://www.thelanternofqz.com

```html
<!DOCTYPE html>
<html lang="en">
<head>
<meta charset="utf-8">
<title>Lumera Health Services</title>
<link rel="stylesheet" href="https://fonts.googleapis.com/css2?family=Poppins:ital,wght@0,300;0,400;0,500;0,600;1,300;1,400;1,500&family=Lexend:wght@500;600&display=swap">
<style>
:root{
  --navy:#0f2240;
  --text:#4a4f58;
  --muted:#6b7079;
  --orange:#f07d23;
  --teal:#9fd9dc;
  --teal-soft:#d7f0f0;
  --white:#ffffff;
  --line:#e2e5e8;
}
*{box-sizing:border-box;margin:0;padding:0}
html,body{width:1200px;height:3282px;overflow:hidden;background:var(--white)}
body{position:relative;font-family:"Poppins",sans-serif;color:var(--text)}
.abs{position:absolute}
h1,h2,h3{font-family:"Lexend",sans-serif;color:var(--navy);font-weight:600}
.btn{position:absolute;display:flex;align-items:center;justify-content:center;border-radius:22px;background:var(--orange);color:var(--white);font-size:15px;font-weight:500;text-transform:uppercase;letter-spacing:.2px}
.btn.ghost{background:var(--white);color:var(--orange)}
.hero-bg{left:0;top:0;width:1200px;height:690px}
.brand{left:60px;top:22px;display:flex;align-items:center;gap:8px}
.brand-dot{width:10px;height:10px;background:var(--orange);border-radius:2px}
.brand-name{font-size:32px;font-weight:500;color:var(--navy);letter-spacing:-.5px;line-height:1}
.brand-sub{position:absolute;left:34px;top:40px;font-size:11px;letter-spacing:7px;color:#8fb9c4}
.nav{top:36px;left:625px;display:flex;gap:33px;font-size:14px;color:var(--navy)}
.nav .active{color:var(--orange);border-bottom:2px solid var(--orange);padding-bottom:6px}
.hero-title{left:60px;top:252px;font-size:48px;line-height:56px}
.hero-text{left:60px;top:372px;width:430px;font-size:13px;line-height:23px;color:var(--text)}
.section-title{width:1200px;left:0;text-align:center;font-size:34px}
.card-img{border-radius:40px 40px 0 40px;height:202px;width:350px}
.card h3{position:absolute;width:350px;text-align:center;font-size:18px;font-weight:500;top:224px;font-family:"Poppins",sans-serif}
.card p{position:absolute;width:350px;text-align:center;font-size:13px;line-height:23px;top:256px;padding:0 40px}
.card .btn{left:107px;top:318px;width:135px;height:36px}
.feature{left:60px;display:flex;gap:16px}
.feature-icon{width:60px;height:60px;border-radius:8px;background:#e9f6f6;display:flex;align-items:center;justify-content:center}
.feature h4{font-size:18px;font-weight:500;color:var(--navy);margin-top:8px}
.feature p{font-size:12.5px;line-height:20px;width:300px;margin-top:10px}
.photo-frame{border-radius:60px 0 0 60px}
.testimonial{left:569px;top:1924px;width:470px;display:flex;flex-direction:column}
.quote-open{display:block}
.quote{margin:-14px 0 0 48px;width:410px;font-size:13px;font-style:italic;font-weight:300;line-height:23px;color:var(--muted)}
.quote-close{display:inline-block;vertical-align:-10px;margin-left:10px}
.quote-author{display:flex;align-items:center;gap:15px;margin:18px 0 0 44px}
.quote-author i{width:18px;height:2px;background:var(--orange)}
.quote-author span{font-size:16px;font-style:italic;font-weight:500;color:var(--orange)}
.form-field{position:absolute;left:60px;width:282px;background:var(--white);border-radius:8px;font-size:11px;padding:12px 15px;color:var(--navy)}
.info-title{font-size:18px;font-weight:500;color:var(--navy)}
.info-row{display:flex;gap:16px;font-size:13px;line-height:19px;color:var(--text);position:absolute;left:489px}
.hours{left:819px;top:2922px;font-size:13px;line-height:24px;color:var(--text)}
.hours b{font-weight:500;color:var(--navy);margin-right:8px}
.social{width:32px;height:32px;border-radius:6px;background:#fde6d3}
</style>
</head>
<body>

<!-- Hero -->
<svg class="abs hero-bg" viewBox="0 0 1200 690" aria-hidden="true">
  <defs>
    <linearGradient id="heroGrad" x1="0" y1="0" x2="1" y2="1">
      <stop offset="0" stop-color="#ffffff"/>
      <stop offset=".55" stop-color="#e2f4f3"/>
      <stop offset="1" stop-color="#9fd9dc"/>
    </linearGradient>
  </defs>
  <path d="M0 0H1200V650C1060 690 940 680 820 640C680 590 540 560 380 575C230 590 90 610 0 675Z" fill="url(#heroGrad)"/>
  <path d="M0 675C120 600 250 560 420 580C560 595 650 660 780 670" fill="none" stroke="#ffffff" stroke-width="10" opacity=".7"/>
</svg>
<svg class="abs" style="left:512px;top:0" width="688" height="690" viewBox="0 0 688 690" role="img" aria-label="Photo of a doctor in a white coat consulting with a smiling patient">
  <defs>
    <linearGradient id="heroPhoto" x1="0" y1="0" x2="1" y2="1">
      <stop offset="0" stop-color="#e4ddd4"/>
      <stop offset=".5" stop-color="#c9b7a6"/>
      <stop offset="1" stop-color="#b45a2c"/>
    </linearGradient>
  </defs>
  <path d="M88 0H688V640C560 675 420 680 300 640C150 590 20 510 0 360C-15 230 20 80 88 0Z" fill="#bfe5e6"/>
  <path d="M98 0H688V630C560 660 420 662 300 625C170 585 40 500 22 360C8 240 40 90 98 0Z" fill="url(#heroPhoto)"/>
</svg>

<div class="abs brand">
  <span class="brand-dot"></span>
  <span class="brand-name">Lumera Health</span>
  <span class="brand-sub">SERVICES</span>
</div>
<nav class="abs nav">
  <span class="active">Home</span><span>Services</span><span>About</span><span>Testimonial</span><span>Appointment</span><span>Contact</span>
</nav>

<h1 class="abs hero-title">Lumera Health<br>Services</h1>
<p class="abs hero-text">Lorem Ipsum is simply dummy text of the printing and typesetting industry. Sed ut perspiciatis unde omnis iste natus error sit voluptatem lorem ipsum dolor</p>
<div class="btn" style="left:60px;top:459px;width:150px;height:41px">Appointment</div>
<div class="btn ghost" style="left:215px;top:459px;width:150px;height:41px">Contact</div>

<!-- Services -->
<h2 class="abs section-title" style="top:740px">Lumera Health Services</h2>
<div class="abs card" style="left:60px;top:816px">
  <div class="card-img" role="img" aria-label="Photo of a trainer guiding a woman through a dumbbell exercise in a gym" style="background:linear-gradient(135deg,#e9e9ea,#cfd3d6 50%,#4a6ea6)"></div>
  <h3>fitness Consultation</h3>
  <p>Lorem Ipsum is simply dummy text of the printing and typesetting industry.</p>
  <div class="btn">Read More</div>
</div>
<div class="abs card" style="left:425px;top:816px">
  <div class="card-img" role="img" aria-label="Photo of a calm woman breathing deeply outdoors" style="background:linear-gradient(135deg,#3f5a3a,#8a7a5a 50%,#c9a33a)"></div>
  <h3>stress management</h3>
  <p>Lorem Ipsum is simply dummy text of the printing and typesetting industry.</p>
  <div class="btn">Read More</div>
</div>
<div class="abs card" style="left:790px;top:816px">
  <div class="card-img" role="img" aria-label="Photo of a counsellor with a tablet talking to a young client" style="background:linear-gradient(135deg,#dfe8e0,#c5cfd6 50%,#8aa2c4)"></div>
  <h3>holistic health</h3>
  <p>Lorem Ipsum is simply dummy text of the printing and typesetting industry.</p>
  <div class="btn">Read More</div>
</div>

<!-- About -->
<svg class="abs" style="left:600px;top:1245px" width="600" height="480" viewBox="0 0 600 480" aria-hidden="true">
  <path d="M60 45L600 5V420C400 440 220 470 90 475C40 476 15 450 12 400V95C12 70 30 50 60 45Z" fill="#a8dcdd"/>
</svg>
<div class="abs photo-frame" role="img" aria-label="Photo of a woman with eyes closed, hands on her chest, relaxing outdoors" style="left:621px;top:1272px;width:579px;height:428px;background:linear-gradient(120deg,#e8e2d0,#c9b98a 45%,#9a8a5a 75%,#6f7a48)"></div>

<h2 class="abs" style="left:62px;top:1322px;font-size:34px">About Lumera Health Services</h2>
<p class="abs" style="left:61px;top:1378px;width:380px;font-size:13px;line-height:23px">Lorem Ipsum is simply dummy text of the printing and typesetting industry. Sed ut perspiciatis unde</p>
<div class="abs" style="left:60px;top:1444px;width:438px;height:1px;background:var(--line)"></div>

<div class="abs feature" style="top:1474px">
  <div class="feature-icon">
    <svg width="30" height="30" viewBox="0 0 30 30" fill="none" stroke="#f07d23" stroke-width="2"><circle cx="15" cy="15" r="12"/><circle cx="15" cy="15" r="7"/><circle cx="15" cy="15" r="2"/><path d="M15 15L25 5"/></svg>
  </div>
  <div><h4>Our Mission</h4><p>At Lumera Health Services, we are committed to providing top-notch health...</p></div>
</div>
<div class="abs feature" style="top:1572px">
  <div class="feature-icon">
    <svg width="30" height="30" viewBox="0 0 30 30" fill="none" stroke="#f07d23" stroke-width="2"><path d="M3 15C7 9 11 7 15 7S23 9 27 15C23 21 19 23 15 23S7 21 3 15Z"/><circle cx="15" cy="15" r="4"/></svg>
  </div>
  <div><h4>Our vission</h4><p>Our team of experienced health consultants has a diverse range of expertise...</p></div>
</div>

<!-- Testimonials -->
<h2 class="abs section-title" style="top:1792px">Customer Testimonials</h2>
<div class="abs" role="img" aria-label="Portrait photo of a smiling customer" style="left:290px;top:1914px;width:208px;height:208px;border-radius:50%;border:3px solid var(--teal);background:radial-gradient(circle at 50% 45%,#c89a7c,#6b4a32 60%,#2f4a3a)"></div>
<div class="abs" role="img" aria-label="Portrait photo of a customer" style="left:254px;top:1860px;width:81px;height:81px;border-radius:50%;background:radial-gradient(circle,#b08c74,#3a3a34)"></div>
<div class="abs" role="img" aria-label="Portrait photo of a customer" style="left:185px;top:1970px;width:81px;height:81px;border-radius:50%;background:radial-gradient(circle,#b8a090,#2e3138)"></div>
<div class="abs" role="img" aria-label="Portrait photo of a customer" style="left:245px;top:2088px;width:81px;height:81px;border-radius:50%;background:radial-gradient(circle,#c09a84,#2c3440)"></div>

<div class="abs testimonial">
  <svg class="quote-open" width="44" height="30" viewBox="0 0 44 30" fill="#9fd9dc" aria-hidden="true"><path d="M0 30V16C0 6 6 0 16 0V6C10 6 8 10 8 14H18V30ZM24 30V16C24 6 30 0 40 0V6C34 6 32 10 32 14H42V30Z"/></svg>
  <p class="quote">Lorem Ipsum has been the industry's standard dummy text ever since the when an unknown printer took a galley of type and scrambled it to make a type industry specimen book. survived not only five centuries, but also the leap into printtype setting text Lorem Ipsum has been the industry...<svg class="quote-close" width="44" height="30" viewBox="0 0 44 30" fill="#9fd9dc" aria-hidden="true"><path d="M44 0V14C44 24 38 30 28 30V24C34 24 36 20 36 16H26V0ZM20 0V14C20 24 14 30 4 30V24C10 24 12 20 12 16H2V0Z"/></svg></p>
  <div class="quote-author"><i></i><span>Dana Whitfield</span></div>
</div>

<!-- Who we are -->
<svg class="abs" style="left:600px;top:2245px" width="600" height="480" viewBox="0 0 600 480" aria-hidden="true">
  <path d="M60 45L600 5V420C400 440 220 470 90 475C40 476 15 450 12 400V95C12 70 30 50 60 45Z" fill="#a8dcdd"/>
</svg>
<div class="abs photo-frame" role="img" aria-label="Photo of a nurse showing a tablet to a smiling senior woman on a sofa" style="left:623px;top:2272px;width:577px;height:428px;background:linear-gradient(120deg,#c8c2ba,#9aa0a4 40%,#3ea0d8 60%,#8f8372)"></div>

<h2 class="abs" style="left:62px;top:2368px;font-size:34px">who we are?</h2>
<p class="abs" style="left:62px;top:2422px;width:420px;font-size:13px;line-height:23px">Lorem Ipsum has been the industry's standard dummy text ever since the 1500s, when an unknown printer took a galley of type and scrambled it to make a type specimen book. It has survived not only five centuries, but also the leap into electronic typesetting, remaining essentially unchanged.</p>
<div class="btn" style="left:60px;top:2560px;width:142px;height:37px">Learn More</div>

<!-- Appointment & footer -->
<svg class="abs" style="left:0;top:2795px" width="440" height="487" viewBox="0 0 440 487" aria-hidden="true">
  <defs>
    <linearGradient id="apptGrad" x1="0" y1="0" x2="1" y2="0">
      <stop offset="0" stop-color="#ffffff"/>
      <stop offset=".55" stop-color="#d9f0f0"/>
      <stop offset="1" stop-color="#9fd9dc"/>
    </linearGradient>
  </defs>
  <path d="M0 8C80 -8 160 10 230 70C330 150 440 240 435 340C430 430 360 480 260 487H0Z" fill="url(#apptGrad)"/>
</svg>
<h2 class="abs" style="left:62px;top:2893px;font-size:32px">Appointment</h2>
<p class="abs" style="left:61px;top:2944px;font-size:12px">Have Any Question please Contact Us!</p>
<div class="form-field" style="top:2978px;height:38px">Name *</div>
<div class="form-field" style="top:3024px;height:37px">Email *</div>
<div class="form-field" style="top:3070px;height:65px">Message *</div>
<div class="btn" style="left:60px;top:3155px;width:120px;height:35px">Submit</div>

<h3 class="abs info-title" style="left:489px;top:2872px">Contact</h3>
<div class="info-row" style="top:2925px">
  <svg width="18" height="18" viewBox="0 0 24 24" fill="#0f2240"><path d="M6.6 10.8a15 15 0 006.6 6.6l2.2-2.2c.3-.3.7-.4 1-.2 1.1.4 2.3.6 3.6.6.6 0 1 .4 1 1V20c0 .6-.4 1-1 1C10.6 21 3 13.4 3 4c0-.6.4-1 1-1h3.5c.6 0 1 .4 1 1 0 1.3.2 2.5.6 3.6.1.3 0 .7-.2 1z"/></svg>
  <span>+ 202-555-0147</span>
</div>
<div class="info-row" style="top:2967px">
  <svg width="18" height="18" viewBox="0 0 24 24" fill="none" stroke="#0f2240" stroke-width="2"><rect x="3" y="8" width="18" height="12" rx="2"/><path d="M7 8V3h10v5M7 13h4M7 16h4"/></svg>
  <span>+ 202-555-0182</span>
</div>
<div class="info-row" style="top:3012px">
  <svg width="18" height="18" viewBox="0 0 24 24" fill="#0f2240"><path d="M2 5h20v14H2z"/><path d="M2 5l10 8 10-8" stroke="#fff" stroke-width="1.8" fill="none"/></svg>
  <span>hello@lumerahealthcare<br>.com</span>
</div>
<div class="info-row" style="top:3073px">
  <svg width="18" height="18" viewBox="0 0 24 24" fill="#0f2240"><path d="M12 2a7 7 0 00-7 7c0 5 7 13 7 13s7-8 7-13a7 7 0 00-7-7zm0 9.5A2.5 2.5 0 1112 6.5a2.5 2.5 0 010 5z"/></svg>
  <span>4810 Alder Row NW,<br>Suite 210 Washington, DC<br>20011</span>
</div>

<h3 class="abs info-title" style="left:819px;top:2872px">Hours</h3>
<div class="abs hours">
  <div><b>Mon</b>09:00 am – 05:00 pm</div>
  <div><b>Tue</b>09:00 am – 05:00 pm</div>
  <div><b>Wed</b>09:00 am – 05:00 pm</div>
  <div><b>Thu</b>09:00 am – 05:00 pm</div>
  <div><b>Fri</b>09:00 am – 05:00 pm</div>
  <div><b>Sat</b>10:00 am – 02:00 pm</div>
  <div><b>Sun</b>Closed</div>
</div>

<div class="abs" style="left:420px;top:3152px;width:720px;height:1px;background:var(--line)"></div>
<div class="abs" style="left:985px;top:3168px;display:flex;gap:8px">
  <span class="social"></span><span class="social"></span><span class="social"></span><span class="social"></span>
</div>
<p class="abs" style="right:62px;top:3218px;font-size:11px;font-weight:600;color:var(--navy)">Copyright © 2025 Lumera Health Services - All Rights Reserved.</p>

</body>
</html>
```